Photography Studio Prep Guide Design Needed

I have a prep guide I send to all parents who book a session - It is outdated and ugly. I want a gorgeous, clean, modern upscale look for the brochure I send.

I already have the text and can provide photos for the final design. I want the cover to be clean and upscale and modern, with a happy feel.

Target Market(s)

My clients for an upscale Newborn Photography Studio

Requirements
Must have
• space for my photos, an upscale clean feel
Nice to have
• I love color, but don't want the brochure to look busy. I love cream, white, pale pink.

```html
<!DOCTYPE html>
<html lang="en">
<head>
<meta charset="utf-8">
<title>Newborn Session Prep Guide</title>
<link href="https://fonts.googleapis.com/css2?family=Raleway:wght@200;300;400;600&family=Oswald:wght@400&family=Parisienne&display=swap" rel="stylesheet">
<style>
:root{
  --rose:#d69aab;
  --rose-deep:#c27a91;
  --rose-soft:#f3dde3;
  --ink:#5a5556;
  --paper:#ffffff;
  --stone:#e6e3e1;
  --cream:#f3ede3;
}
*{margin:0;padding:0;box-sizing:border-box}
html,body{width:974px;height:1200px;overflow:hidden;background:#fff}
body{position:relative;font-family:"Raleway",sans-serif;color:var(--ink)}
.panel{position:absolute;width:309px;height:387px;overflow:hidden;background:var(--paper)}
.frame{position:absolute;inset:5px;border:1px solid var(--rose)}
.photo{position:absolute}
.copy{position:absolute;left:14px;right:14px;font-size:5.1px;line-height:1.38}
.copy p{margin-bottom:2px}
.copy b{font-weight:600}
.sec{font-family:"Oswald",sans-serif;color:var(--rose-deep);font-size:8.4px;letter-spacing:.2px;margin:6px 0 3px;text-transform:uppercase}
.script{font-family:"Parisienne",cursive;color:var(--rose-deep);text-align:center}
.center{text-align:center}
.qbar{display:table;margin:5px auto 3px;background:var(--rose);color:#fff;font-family:"Oswald",sans-serif;font-size:7px;padding:1px 6px;text-transform:uppercase}
.faq-title{font-family:"Oswald",sans-serif;color:var(--rose-deep);font-size:15px;text-align:center}
/* cover */
.cover{background:var(--rose)}
.cover .frame{border-color:#fff}
.cover-brand{position:absolute;left:0;right:0;top:68px;text-align:center;color:#fff;font-size:11px;letter-spacing:2px;font-weight:300}
.cover-brand .ring{display:block;width:86px;height:86px;border:1px solid #fff;border-radius:50%;margin:-34px auto 0;position:relative;top:-10px}
.cover-title{position:absolute;left:0;right:0;top:164px;text-align:center;color:#fff;font-weight:200;font-size:23px;letter-spacing:.5px}
.cover-sub{position:absolute;left:0;right:0;top:186px;text-align:center;color:#fff;font-family:"Parisienne",cursive;font-size:27px}
.steps{position:absolute;left:14px;right:14px;font-size:5.1px;line-height:1.38}
.step{display:flex;gap:8px;margin-bottom:9px;align-items:flex-start}
.num{flex:0 0 17px;height:17px;border-radius:50%;background:var(--rose);color:#fff;font-family:"Oswald",sans-serif;font-size:9px;text-align:center;line-height:17px}
.roundpic{position:absolute;width:70px;height:70px;border-radius:50%}
.contact{position:absolute;left:0;right:0;text-align:center;color:#6b6566}
</style>
</head>
<body>

<!-- Cover -->
<section class="panel cover" style="left:22px;top:16px">
  <div class="frame"></div>
  <div class="cover-brand"><span class="ring"></span>CLARA WHITFIELD<br><span style="font-size:7px;letter-spacing:3px">PHOTOGRAPHY</span></div>
  <div class="cover-title">NEWBORN SESSION</div>
  <div class="cover-sub">Prep Guide</div>
  <div class="photo" role="img" aria-label="Smiling baby wearing a floral crown lying on a pink blanket" style="left:60px;top:250px;width:190px;height:130px;background:radial-gradient(ellipse at 50% 45%,#f1d3c4 0%,#e2b0b6 55%,var(--rose) 100%)"></div>
</section>

<!-- Parent instructions -->
<section class="panel" style="left:331px;top:16px">
  <div class="frame"></div>
  <div class="center" style="position:absolute;top:16px;left:0;right:0;font-size:6px;letter-spacing:1.5px;color:var(--rose-deep)">CLARA WHITFIELD</div>
  <div class="script" style="position:absolute;top:46px;left:0;right:0;font-size:14px">Parent Instructions &amp; Preparations</div>
  <div class="copy" style="top:72px">
    <p class="center">Congratulations on expecting a baby!<br>Here are my instructions to ensure a successful newborn photography session.<br>Please follow these instructions as closely as possible.</p>
    <div class="sec">1. Nursing</div>
    <p>If you are nursing, please avoid eating anything spicy (hot sauce, hot peppers, curry, etc.) that might upset baby's tummy for 24 hours preceding your scheduled session. Please if you are breastfeeding do NOT drink caffeine or coffee before your session – I know this is hard but baby will be wired if you have caffeine. If you notice baby has a lot of gas after feedings please check with your pediatrician and bring gas drops to your session. The most common reason a baby will not settle for a session is gas pressure/discomfort.</p>
    <div class="sec">2. Feeding</div>
    <p>Feed the baby as much as possible in the 24 hours preceding your session – this will help minimize the amount baby needs to feed during the session, and will help baby sleep as long and as soundly as possible. Feed baby 2-3 hours before your session and not again until you arrive. <b>Please bring an extra bottle of formula or breastmilk to the session if possible – sometimes a small amount of milk in a bottle can quickly soothe a baby back to sleep without requiring a full feeding.</b> I will respect your wishes if you choose not to use a bottle.</p>
  </div>
  <div class="photo" role="img" aria-label="Mother lifting her baby in the air on a white background" style="left:85px;top:262px;width:195px;height:119px;background:linear-gradient(180deg,#fdfcfb,#efe6e1 70%,#e7ddd8)"></div>
</section>

<!-- Sections 3-7 -->
<section class="panel" style="left:641px;top:16px">
  <div class="frame"></div>
  <div class="photo" role="img" aria-label="Newborn with a headband resting on a pink wrap" style="left:6px;top:6px;width:297px;height:52px;background:linear-gradient(90deg,#f1c9d0,#f7e2e4 50%,#eab9c4)"></div>
  <div class="copy" style="top:58px">
    <div class="sec">3. Keep Baby Awake</div>
    <p>Interact with, and <b>keep baby awake for 2 hours preceding your appointment to make sure they are nice and sleepy for their session.</b> A great way to do this is by giving baby a bath – which will get them nice and clean and keep them awake. Also – keeping baby naked, in a diaper only is a good way to keep them awake and alert. <b>This step is extremely important – otherwise it can take a long time to get baby to sleep.</b></p>
    <div class="sec">4. Clothes</div>
    <p>Please dress baby in a simple loose sleeper we can just unsnap when you arrive – we want to keep baby as calm and happy as possible and avoid clothes we have to pull over their head. I provide all clothing/hats/props at your session.</p>
    <div class="sec">5. Pacifier</div>
    <p>Please bring a pacifier – it can be very helpful during a session if a baby is fussy. Please note I only use the pacifier for a few minutes at a time to soothe into a pose. <b>If you choose not to bring a pacifier I will respect your decision, but please understand we may have to pass on several poses.</b></p>
    <div class="sec">6. Studio</div>
    <p>My studio is kept VERY warm to make sure your baby is comfortable through the whole session. It will be around 75-80 degrees so please dress in layers for comfort. I will have cold bottles of water available during your session. <b>Please note – if you ask me to turn the heat down, or tell me it is too warm for baby, I cannot guarantee any results for your session.</b> Babies are used to 98.6 degrees in the womb, and a cold studio will wake baby immediately.</p>
    <div class="sec">7. Your Role</div>
    <p>Your role at this session is to sit back and relax. I need very little assistance during the session, and want you to take this time to rest, relax and enjoy the session. Feel free to nap, catch up on work, thank you notes, or whatever you like. If baby needs to feed during the session that will be your only task! I will occasionally ask for a spotter for safety on some poses.</p>
  </div>
</section>

<!-- Sections 8-10 -->
<section class="panel" style="left:22px;top:402px">
  <div class="frame"></div>
  <div class="copy" style="top:10px">
    <div class="sec">8. Time</div>
    <p>Your session will last between 2-4 hours – please keep this in mind. I will provide bottled water and light snacks (granola bars/pretzels/etc.) but you may want to bring more food since the session can last up to 4 hours. <b>Please note that I cannot shoot past 4 hours – if baby is still fussy I will do my best to get beautiful photos. At 3 hours if baby is still fussy I will let you know that we need to switch to swaddled/wrapped poses to finish the session. Or we can do more family photos as well.</b></p>
  </div>
  <div class="photo" role="img" aria-label="Newborn in a white knit nest" style="left:6px;top:98px;width:97px;height:101px;background:linear-gradient(160deg,#f6f0ea,#e4d9cf)"></div>
  <div class="photo" role="img" aria-label="Newborn curled in a mint wrap" style="left:106px;top:98px;width:97px;height:101px;background:linear-gradient(160deg,#d9ece6,#a9d3c8)"></div>
  <div class="photo" role="img" aria-label="Newborn in a purple floral nest" style="left:206px;top:98px;width:97px;height:101px;background:linear-gradient(160deg,#8c6d9a,#5f4870)"></div>
  <div class="copy" style="top:206px">
    <div class="sec">9. Family Photos/Clothing</div>
    <p>I highly recommend mom and dad wear simple white/cream shirts, or black/navy shirts which will keep the focus on the baby. Mom can choose a tank top or dress as well. That is only a suggestion, and of course you are welcome to wear anything you choose. If dad is comfortable baring his chest it can make for some beautiful images, but that is totally up to the comfort of dad! My photos of newborns with mom/dad are generally from the waist up, so your pants or shoes will not matter.</p>
    <div class="sec">10. Sibling Photo</div>
    <p>Photos of your newborn with their sibling(s) are included, and will be done at the very beginning of the session. I recommend having sibling boys wear cream/white tops or plain dark shirts with jeans. Sibling girls can wear cream/white shirts/tank tops with jeans or cream/white dresses.</p>
    <p><b>I do not recommend bringing toddlers/children for the entire session. It is very hot in my studio and there is not adequate room for them to play. Please plan to bring them for photos at the beginning of the session, and have dad or a grandparent take them out for an activity while we finish the session.</b></p>
  </div>
</section>

<!-- Full photo -->
<section class="panel" style="left:331px;top:402px">
  <div class="photo" role="img" aria-label="Toddler sitting beside a cake smash with paper flowers on a cream backdrop" style="inset:0;background:radial-gradient(ellipse at 50% 60%,#f4eee3 0%,#ece3d4 60%,#e3d7c5 100%)"></div>
</section>

<!-- Before your session + FAQ -->
<section class="panel" style="left:641px;top:402px">
  <div class="frame"></div>
  <div class="script" style="position:absolute;top:14px;left:0;right:0;font-size:14px">What I need to know before your session</div>
  <div class="steps" style="top:40px">
    <div class="step"><span class="num">1</span><span>Please e-mail me with the baby's birth date, birth weight, sex, and name. Remember, my newborn sessions take place between 5-11 days old, so it is critical to e-mail me when baby arrives to schedule your session.</span></div>
    <div class="step"><span class="num">2</span><span>If you have any favorite colors please feel free to let me know and I will be happy to work them into your session. Please also let me know if there are any colors you do not want used during your session.</span></div>
    <div class="step"><span class="num">3</span><span>If you have specific shots in mind for your session, or any props you have seen on my website that you would like me to use, you must let me know in advance.</span></div>
    <div class="step"><span class="num">4</span><span>Please let me know if you have any siblings you would like to include in the session and their age(s).</span></div>
  </div>
  <div class="faq-title" style="position:absolute;top:170px;left:0;right:0">FAQ'S</div>
  <div class="copy center" style="top:192px">
    <div class="qbar">When will I see my photos?</div>
    <p>Your gallery of images will be e-mailed to you within 3 weeks. You will receive a preview photo of your session within 2 days.</p>
    <div class="qbar">Can I share my gallery?</div>
    <p>Yes, you can share your gallery with anyone you like. Just send them the gallery link and password.</p>
    <div class="qbar">How can I download my photos?</div>
    <p>You can download all of your high-resolution images directly from your gallery. Please keep in mind that these are very large files – each photo can be up to 10 megabytes.</p>
  </div>
  <div class="roundpic" role="img" aria-label="Sleeping newborn in a lavender bonnet" style="left:18px;top:305px;background:radial-gradient(circle,#d8c3dd,#a98db3)"></div>
  <div class="roundpic" role="img" aria-label="Baby sitting with a plush teddy bear" style="left:120px;top:305px;background:radial-gradient(circle,#fbfaf8,#ece6e0)"></div>
  <div class="roundpic" role="img" aria-label="Sleeping newborn close-up" style="left:222px;top:305px;background:radial-gradient(circle,#f2ddd1,#dfc0ae)"></div>
</section>

<!-- FAQ continuation -->
<section class="panel" style="left:22px;top:790px">
  <div class="frame"></div>
  <div class="faq-title" style="position:absolute;top:12px;left:0;right:0;font-size:13px">FAQ'S CONTINUATION...</div>
  <div class="copy center" style="top:30px;font-size:5px">
    <div class="qbar">What if my baby won't sleep during session?</div>
    <p>It is very rare that I cannot get a baby to sleep/settle during their session, but when it does happen I focus on getting images of baby when they are calm and awake. This will involve more photos of baby swaddled/wrapped or in mom or dad's arms. Following my instructions before your session will decrease the odds of this happening. I cannot put an awake baby in any props – please keep this in mind. At 3 hours if baby is still fussy I will finish the session with swaddled/wrapped shots, and more shots with mom and dad. I cannot shoot past 4 hours if baby is unable to settle. Again, a pacifier will help greatly in this situation.</p>
    <div class="qbar">What poses will you do?</div>
    <p>This completely depends on the baby. Some babies will go into every pose comfortably and some will not. I pay close attention to your baby's signals, and to what positions are most comfortable for them. I will not force a baby into any position they don't like for a photo. Your baby's comfort and safety is my primary concern at all times. Awake babies cannot go in any props safely; they can only be photographed lying on their backs or in someone's arms.</p>
    <div class="qbar">Will my baby be safe?</div>
    <p>My main focus during the entire session is your baby's safety and comfort. I know you have trusted me with your baby, and I take it very seriously. I thoroughly wash my hands before your session, and use hand sanitizer before and during your session. I have taken numerous newborn safety/photography classes and know what positions are safe for baby. I will always be within reaching distance of your baby, and will have a parent be a spotter if I need to move back any further. Many of my images that you see are composites – meaning mom or dad is sitting right there holding baby's head, and I photoshop them out afterwards.</p>
    <div class="qbar">My baby has acne/scratches/red marks – will those show up in photos?</div>
    <p>No, this is very common and I will photoshop out any scratches/redness/acne.</p>
    <div class="qbar">How many props can I choose?</div>
    <p>A typical session includes around 9 family shots (individual mom, individual dad, whole family, etc.), 6 shots on the beanbag just featuring baby in poses, macro shots of baby's feet, lips, hands and then 2-3 prop setups. Baby will generally not tolerate too many prop shots and outfit changes, so please pick your top 3 and we will see how baby does. If baby is not sleepy I cannot use props for safety reasons. I will always have a variety of beautiful options ready in case baby will not sleep.</p>
  </div>
</section>

<!-- Collage -->
<section class="panel" style="left:331px;top:790px">
  <div class="photo" role="img" aria-label="Newborn sleeping in a small red wagon with a flag backdrop" style="left:0;top:0;width:188px;height:85px;background:linear-gradient(180deg,#d9d2cb,#b98a86 60%,#9b6f5c)"></div>
  <div class="photo" role="img" aria-label="Toddler standing by a white step ladder" style="left:190px;top:0;width:119px;height:181px;background:linear-gradient(180deg,#dbe9ee,#f3f0ea)"></div>
  <div class="photo" role="img" aria-label="Newborn in a red bonnet beside a knitted sock monkey" style="left:0;top:87px;width:188px;height:94px;background:linear-gradient(135deg,#c9c1b6,#a38d79)"></div>
  <div class="photo" role="img" aria-label="Smiling baby with flower crown in a blue wooden tub" style="left:0;top:183px;width:136px;height:204px;background:linear-gradient(180deg,#cfc6bc,#9fbcc0 70%,#c8b9a8)"></div>
  <div class="photo" role="img" aria-label="Newborn in a green knit hat on a cream blanket" style="left:138px;top:183px;width:171px;height:101px;background:linear-gradient(135deg,#f8f4ee,#e4dbcf)"></div>
  <div class="photo" role="img" aria-label="Twin babies in blue outfits on a pink backdrop" style="left:138px;top:286px;width:171px;height:101px;background:linear-gradient(180deg,#f4d6dd,#e9c3cc)"></div>
</section>

<!-- Back cover -->
<section class="panel" style="left:641px;top:790px;background:var(--stone)">
  <div class="contact" style="top:90px;font-size:6px;letter-spacing:.5px">FOR MORE INFO:</div>
  <div class="contact" style="top:100px;font-size:11px;font-weight:300">+1 555-014-2290</div>
  <div class="contact" style="top:118px;font-size:9px;font-weight:300">www.clarawhitfieldphotography.com</div>
  <div class="photo" role="img" aria-label="Smiling baby in a floral bonnet sitting in a white bucket" style="left:70px;top:200px;width:239px;height:187px;background:radial-gradient(ellipse at 55% 45%,#eadfd4 0%,#d5d8cc 50%,var(--stone) 100%)"></div>
</section>

</body>
</html>
```